IT Professional business card with a hometown feel and a little edgy.

My business name is Pebble Website Solutions. But I have ended up doing much more. I live in a very small remote community, where everyone knows everyone. We like the one-on-one customer service in this community. I do computer tutoring, virus removal, networking, and software training. My clients are businesses and private individuals.

My website is pebblewebsitesolutions.example, when I first designed it I was going for a fresh, clean look, which I still like. But I am thinking about making the website a bit more edgy to match my new logo from ArtGrovely (logo attached). At this time my website does not display the new logo, but I plan on redesigning the website in the future to match the logo and business card.

My tag line is "let the internet work for you"

I'm thinking I would like to have the business card printed with a metallic finish.

Please do not use black backgrounds, or any solid dark colors. Prefer light or white backgrounds.

Target Market(s)

Small businesses. Individuals that need computer help at home.

Industry/Entity Type

It Company

Contact Information for Business Card

Marla Dunovan
Pebble Website Solutions
PO Box 7153
Forks, WA 98331
Cell: 360-555-0172
marla@pebblewebsitesolutions.example
pebblewebsitesolutions.example

Font styles to use
Serif

Requirements
Must have
• Must have all the information listed in "Business Card Details"
• Must use the logo provided.
• Use the colors from the provided logo
Nice to have
• Would like to use my tagline "let the internet work for you" all lowercase

```html
<!DOCTYPE html>
<html lang="en">
<head>
<meta charset="utf-8">
<title>Pebble Website Solutions – Business Card</title>
<link rel="stylesheet" href="https://fonts.googleapis.com/css2?family=Source+Serif+4:opsz,wght@8..60,400;8..60,600&display=swap">
<style>
  :root {
    --backdrop: #eceae6;
    --card-white: #ffffff;
    --green-dark: #1f5e2e;
    --green-mid: #3f8a45;
    --green-light: #6fae5f;
    --green-glow: #78b06b;
    --ink: #333333;
    --back-mark: rgba(190, 225, 180, 0.55);
  }
  * { box-sizing: border-box; margin: 0; padding: 0; }
  html, body {
    width: 1200px; height: 900px; overflow: hidden;
    background: var(--backdrop);
    font-family: "Source Serif 4", Georgia, serif;
  }
  .canvas { position: relative; width: 1200px; height: 900px; }

  .card {
    position: absolute; width: 640px; height: 365px; overflow: hidden;
    box-shadow: 0 6px 18px rgba(0,0,0,0.18);
  }

  /* Back of card */
  .card-back {
    left: 470px; top: 60px;
    background: radial-gradient(ellipse at 50% 45%, var(--green-glow) 0%, var(--green-mid) 45%, var(--green-dark) 100%);
  }
  .back-lockup {
    position: absolute; left: 150px; top: 95px;
    display: flex; align-items: center; gap: 22px;
  }
  .back-lockup .mark-square {
    width: 70px; height: 70px; border: 4px solid var(--back-mark);
  }
  .back-lockup .brand-name {
    color: var(--back-mark); font-size: 32px; line-height: 1.05; font-weight: 400;
  }
  .tagline {
    position: absolute; left: 0; right: 0; top: 262px;
    text-align: center; color: #ffffff; font-size: 19px;
  }

  /* Front of card */
  .card-front { left: 90px; top: 490px; background: var(--card-white); }
  .card-bands { position: absolute; inset: 0; }
  .person { position: absolute; left: 48px; top: 34px; }
  .person-name { font-size: 25px; font-weight: 600; color: var(--ink); line-height: 1.15; }
  .person-role { font-size: 15px; color: var(--green-dark); }

  .contact-list { position: absolute; left: 48px; top: 128px; list-style: none; }
  .contact-list li {
    display: flex; align-items: center; gap: 9px;
    font-size: 15px; color: var(--ink); line-height: 22px;
  }
  .contact-list svg { width: 13px; height: 13px; fill: var(--green-dark); flex: none; }
  .address { position: absolute; left: 48px; top: 202px; font-size: 15px; color: var(--ink); line-height: 21px; }

  .front-lockup {
    position: absolute; left: 400px; top: 118px;
    display: flex; align-items: center; gap: 16px;
  }
  .front-lockup .mark-square {
    width: 52px; height: 52px; background: var(--green-dark);
  }
  .front-lockup .brand-name {
    color: var(--green-dark); font-size: 24px; line-height: 1.05; font-weight: 400;
  }
</style>
</head>
<body>
<main class="canvas">

  <section class="card card-back" aria-label="Card back">
    <div class="back-lockup">
      <span class="mark-square"></span>
      <span class="brand-name">Pebble<br>Website<br>Solutions</span>
    </div>
    <p class="tagline">"let the internet work for you"</p>
  </section>

  <section class="card card-front" aria-label="Card front">
    <svg class="card-bands" viewBox="0 0 640 365" width="640" height="365" aria-hidden="true">
      <polygon points="0,262 292,262 278,290 0,290" fill="var(--green-light)"/>
      <polygon points="300,298 640,298 640,365 268,365" fill="var(--green-dark)"/>
    </svg>

    <div class="person">
      <p class="person-name">Marla Dunovan</p>
      <p class="person-role">Managing Director</p>
    </div>

    <ul class="contact-list">
      <li>
        <svg viewBox="0 0 16 16"><path d="M3 2c1-1 2-1 3 0l1.5 2c.5.8.3 1.5-.3 2L6.5 7c.8 1.5 1.8 2.6 3.4 3.4l1-.8c.6-.5 1.3-.7 2-.2l2 1.5c1 .9 1 2 0 3-2 2-5 1.5-8.5-2S1 4 3 2z"/></svg>
        Cell: 360-555-0172
      </li>
      <li>
        <svg viewBox="0 0 16 16"><path d="M1 3h14v10H1zm1.5 1.2L8 8.5l5.5-4.3z"/></svg>
        marla@pebblewebsitesolutions.example
      </li>
      <li>
        <svg viewBox="0 0 16 16"><path d="M8 1a7 7 0 1 0 0 14A7 7 0 0 0 8 1zm0 1.5a5.5 5.5 0 0 1 0 11 5.5 5.5 0 0 1 0-11zM2.5 7.3h11v1.4h-11zM7.3 2.5h1.4v11H7.3z"/></svg>
        pebblewebsitesolutions.example
      </li>
    </ul>

    <p class="address">PO Box 7153<br>Forks, WA 98331</p>

    <div class="front-lockup">
      <span class="mark-square"></span>
      <span class="brand-name">Pebble<br>Website<br>Solutions</span>
    </div>
  </section>

</main>
</body>
</html>
```